Business Card Design

Just looking for a good designs that looks good with our company logo. I'd like it to be simple and to the point. Just including contact information, our logo, and my name somewhere on the card so future clients know who they're contacting, and a couple services offered. The two images I attached are pictures of our logo. I don't care which color they they are, I just attached both images to give a reference of logo colors depending on the color of the card.
Names: Derek Hallory
Phone: 816-442-7061
Email: greenvalebrush@mailzen.test
Services offered:
Mowing
Fertilization
Aeration
Bed & tree maintenance
and more.
Industry/Entity Type
Business
Contact Information for Business Card
Names: Derek Hallory
Phone: 816-442-7061
Look and feel

```html
<!DOCTYPE html>
<html lang="en">
<head>
<meta charset="utf-8">
<title>Greenvale Lawn &amp; Landscape – Business Card</title>
<link rel="stylesheet" href="https://fonts.googleapis.com/css2?family=Open+Sans:wght@400;600;700&display=swap">
<style>
  :root {
    --backdrop: #e6e6e6;
    --navy: #1f212b;
    --signal-red: #e2371f;
    --grass-dark: #3f8f22;
    --grass-light: #6cc23c;
    --white: #ffffff;
    --muted: #c9cad0;
  }
  * { box-sizing: border-box; margin: 0; padding: 0; }
  html, body { width: 1200px; height: 1200px; overflow: hidden; }
  body {
    background: radial-gradient(circle at 50% 40%, #f4f4f4, var(--backdrop));
    font-family: "Open Sans", Arial, sans-serif;
    position: relative;
  }
  .business-card {
    position: absolute;
    left: 100px; top: 314px;
    width: 1000px; height: 572px;
    background: var(--navy);
    overflow: hidden;
    box-shadow: 0 18px 40px rgba(0,0,0,.18);
  }
  .grass-field {
    position: absolute; left: 0; top: 0; width: 100%; height: 150px;
    background: linear-gradient(160deg, var(--grass-light), var(--grass-dark) 70%, #4fa52b);
  }
  .red-band {
    position: absolute; left: 0; top: 150px; width: 100%; height: 50px;
    background: var(--signal-red);
  }
  .services-panel {
    position: absolute; left: 530px; top: 150px; width: 470px; height: 120px;
    background: var(--signal-red);
    padding: 18px 0 0 28px;
    color: var(--white);
    font-size: 21px; line-height: 29px;
  }
  .service-line { display: flex; align-items: center; gap: 8px; white-space: nowrap; }
  .tick { width: 18px; height: 18px; flex: none; }
  .brand-mark {
    position: absolute; left: 50px; top: 115px;
    display: flex; align-items: center; gap: 18px;
  }
  .brand-circle {
    width: 120px; height: 120px; border-radius: 50%; flex: none;
    background: var(--signal-red); border: 6px solid var(--white);
  }
  .brand-name {
    font-weight: 700; font-size: 30px; color: var(--white);
    line-height: 1.15; letter-spacing: 1px; white-space: nowrap;
  }
  .contact-block {
    position: absolute; left: 560px; top: 345px; color: var(--muted);
  }
  .person-name {
    color: var(--white); font-weight: 700; font-size: 30px; margin-bottom: 14px;
  }
  .contact-line {
    display: flex; align-items: center; gap: 14px;
    font-size: 25px; line-height: 36px;
  }
  .contact-icon { width: 22px; height: 22px; flex: none; }
</style>
</head>
<body>
  <div class="business-card">
    <div class="grass-field" role="img" aria-label="Photograph of freshly mown green lawn"></div>
    <div class="red-band"></div>

    <div class="services-panel">
      <div class="service-line">Services offered:</div>
      <div class="service-line">
        <svg class="tick" viewBox="0 0 18 18"><rect width="18" height="18" rx="2" fill="#1f212b"/><path d="M4 9.5l3.2 3L14 5.5" stroke="#fff" stroke-width="2.4" fill="none"/></svg>Mowing
        <svg class="tick" viewBox="0 0 18 18"><rect width="18" height="18" rx="2" fill="#1f212b"/><path d="M4 9.5l3.2 3L14 5.5" stroke="#fff" stroke-width="2.4" fill="none"/></svg>Fertilization
        <svg class="tick" viewBox="0 0 18 18"><rect width="18" height="18" rx="2" fill="#1f212b"/><path d="M4 9.5l3.2 3L14 5.5" stroke="#fff" stroke-width="2.4" fill="none"/></svg>Aeration
      </div>
      <div class="service-line">
        <svg class="tick" viewBox="0 0 18 18"><rect width="18" height="18" rx="2" fill="#1f212b"/><path d="M4 9.5l3.2 3L14 5.5" stroke="#fff" stroke-width="2.4" fill="none"/></svg>Bed &amp; tree maintenance and more.
      </div>
    </div>

    <div class="brand-mark">
      <div class="brand-circle"></div>
      <div class="brand-name">GREENVALE<br>LAWN &amp; LANDSCAPE</div>
    </div>

    <div class="contact-block">
      <div class="person-name">Derek Hallory</div>
      <div class="contact-line">
        <svg class="contact-icon" viewBox="0 0 22 22"><circle cx="11" cy="11" r="11" fill="#e2371f"/><path d="M7.5 5.5h2.5l1 3-1.5 1c.8 1.6 1.8 2.6 3.4 3.4l1-1.5 3 1v2.5c-5 .5-9.9-4.4-9.4-9.4z" fill="#fff"/></svg>
        816-442-7061
      </div>
      <div class="contact-line">
        <svg class="contact-icon" viewBox="0 0 22 22"><circle cx="11" cy="11" r="11" fill="#e2371f"/><rect x="5.5" y="7" width="11" height="8" rx="1" fill="#fff"/><path d="M5.8 7.4L11 11.4l5.2-4" stroke="#e2371f" stroke-width="1.3" fill="none"/></svg>
        greenvalebrush@mailzen.test
      </div>
    </div>
  </div>
</body>
</html>
```